Ironbark Shift Workforce

We are a underground coal mining labour hire company, needing a website that links into our online payroll (www.wagetrackly.com.au) and also need to have job applications page that is a preform with drop down menu,s with answers or check boxes. We would also need a 3 tier administration access for access to different files.
We are looking for an ongoing relationship with future app integration

Reason: There are a few more designs to come and I'm out at the mine for another week

Industry/Entity Type

Coal Mining

```html
<!DOCTYPE html>
<html lang="en">
<head>
<meta charset="utf-8">
<title>Ironbark Shift Workforce</title>
<link href="https://fonts.googleapis.com/css2?family=Arimo:wght@400;700&display=swap" rel="stylesheet">
<style>
:root{
  --orange:#f57c00;
  --orange-light:#ff9a1f;
  --link-orange:#e06a00;
  --black:#0c0c0c;
  --dark:#2e2e2e;
  --dark-line:#1c1c1c;
  --text-dark:#222;
  --text-muted:#999;
  --text-light:#eee;
  --link-grey:#8a8a8a;
  --rule:#dcdcdc;
  --page-grey:#d6d6d6;
}
*{box-sizing:border-box;margin:0;padding:0}
html,body{width:980px;height:1200px;overflow:hidden}
body{font-family:"Arimo",Arial,sans-serif;color:var(--text-dark);background:linear-gradient(#fff 0,#e9e9e9 40px,#fff 300px,#fff 1117px,var(--page-grey) 1117px);position:relative}
.abs{position:absolute}
a{color:inherit}

/* top bar */
.topbar{left:20px;top:0;width:939px;height:36px;background:var(--black);color:#ddd;font-size:12px}
.clock{left:62px;top:11px;display:flex;align-items:center;gap:6px}
.search-field{left:710px;top:8px;width:138px;height:20px;background:#fff;border:0}
.btn-orange{background:var(--orange);color:#fff;font-size:11px;border-radius:4px;text-align:center;text-transform:uppercase}
.search-btn{left:854px;top:8px;width:64px;height:20px;line-height:20px}

/* header */
.brand{left:20px;top:36px;width:252px;height:306px;background:var(--black);display:flex;flex-direction:column;align-items:center;justify-content:center;gap:14px}
.brand-mark{width:34px;height:34px;border-radius:50%;background:var(--orange)}
.brand-name{color:var(--orange);font-size:17px;font-weight:700;text-align:center;line-height:1.3}
.hero{left:273px;top:38px;width:434px;height:284px;background:linear-gradient(120deg,#5f8fc7 0%,#9cc0e6 35%,#efefef 60%,#c7b35a 80%,#8a7a3a 100%)}
.hero-bar{left:273px;top:322px;width:434px;height:20px;background:var(--dark-line);color:#fff;font-size:12px}
.hero-bar span{position:absolute;right:10px;top:3px;display:flex;gap:6px;align-items:center;text-decoration:underline}
.nav{left:708px;top:36px;width:251px;height:306px;background:linear-gradient(135deg,var(--orange-light),var(--orange))}
.nav ul{list-style:none;position:absolute;left:38px;top:55px}
.nav li{color:#fff;font-size:14px;height:28px;display:flex;align-items:center;gap:10px;padding-left:22px;width:175px}
.nav li.current{background:#fff;color:var(--text-dark);border-radius:14px;padding-left:6px;margin-left:-16px;width:175px}
.nav .dot{width:13px;height:13px;border-radius:50%;background:#fff;display:inline-flex;align-items:center;justify-content:center}
.nav .current .dot{background:none}

/* columns */
.col-left{left:20px;top:342px;width:252px;height:775px;background:#fff}
.col-center{left:273px;top:342px;width:434px;height:808px;background:var(--dark)}
.col-right{left:708px;top:342px;width:251px;height:775px;background:#fff}
.heading{font-size:17px;text-transform:uppercase;display:flex;align-items:center;gap:8px;border-bottom:1px solid var(--rule);padding-bottom:4px}
.col-center .heading{color:#aaa;border:0}

.services{left:18px;top:28px;width:212px}
.services ul{list-style:none;margin-top:12px}
.services li{font-size:12px;height:27.5px;line-height:27px;border-bottom:1px solid #eee;display:flex;gap:10px}
.more{display:flex;align-items:center;gap:8px;font-size:12px;text-decoration:underline}
.more .dot{width:14px;height:14px;border-radius:50%;background:#eee}
.more.orange{color:var(--link-orange)}
.double-rule{height:4px;border-top:2px solid #ccc;border-bottom:1px solid #ccc}
.contacts{left:18px;top:542px;width:212px;font-size:12px}
.contacts address{font-style:normal;color:var(--link-orange);margin-top:24px;line-height:16px}
.contacts dl{margin-top:22px;display:grid;grid-template-columns:86px 1fr;line-height:16px}

.text-link{color:var(--link-grey);text-decoration:underline;font-size:12px}
.body-copy{color:var(--text-light);font-size:12px;line-height:15px}
.thumb{border:3px solid #ddd;background:linear-gradient(#5a5a4a,#9a8a50 60%,#3a3a30)}
.divider{height:4px;background:var(--dark-line)}
.link-row{display:flex;gap:36px}
.link-row .more{color:var(--link-grey)}
.link-row .dot{background:#888}
.investor{width:120px;height:140px;border:3px solid #ddd}

.login{left:6px;top:28px;width:216px;font-size:12px}
.field{display:flex;align-items:center;justify-content:space-between;margin-top:8px}
.field span{width:66px}
.field div{width:150px;height:20px;border:1px solid #888}
.jobs{left:6px;top:226px;width:216px}
.job{border-bottom:1px solid #eee;padding:6px 0 8px;margin-top:3px}
.job a{color:var(--link-orange);font-weight:700;font-size:12px}
.job time{display:block;color:var(--text-muted);font-size:11px;margin-top:2px}

.footer{left:0;top:1164px;width:980px;text-align:center;font-size:11px;color:#222}
</style>
</head>
<body>

<header>
  <div class="abs topbar">
    <div class="abs clock"><svg width="8" height="8" viewBox="0 0 8 8"><circle cx="4" cy="4" r="3" fill="none" stroke="#ddd"/></svg>10:32AM, SAT MAR 22</div>
    <div class="abs search-field"></div>
    <div class="abs btn-orange search-btn">Search</div>
  </div>

  <div class="abs brand">
    <span class="brand-mark"></span>
    <span class="brand-name">Ironbark Shift<br>Workforce</span>
  </div>

  <div class="abs hero" role="img" aria-label="Yellow front loader scooping white material under blue sky"></div>
  <div class="abs hero-bar"><span><svg width="13" height="13" viewBox="0 0 13 13"><circle cx="6.5" cy="6.5" r="6.5" fill="#777"/><path d="M4 6.5h5M7 4.5l2 2-2 2" stroke="#fff" fill="none"/></svg>Stop Slideshow</span></div>

  <nav class="abs nav">
    <ul>
      <li class="current"><span class="dot"><svg width="10" height="8" viewBox="0 0 10 8"><path d="M0 4h8M5 1l3 3-3 3" stroke="#222" fill="none"/></svg></span>Home page</li>
      <li><span class="dot"></span>Company overview</li>
      <li><span class="dot"></span>Mining services</li>
      <li><span class="dot"></span>Projects</li>
      <li><span class="dot"></span>Human resources</li>
      <li><span class="dot"></span>Investors</li>
      <li><span class="dot"></span>Contacts</li>
    </ul>
  </nav>
</header>

<aside class="abs col-left">
  <section class="abs services">
    <h2 class="heading"><svg width="16" height="16" viewBox="0 0 16 16"><circle cx="8" cy="8" r="5" fill="none" stroke="#333" stroke-width="2" stroke-dasharray="2 1.5"/><circle cx="8" cy="8" r="2" fill="none" stroke="#333"/></svg>Our Services</h2>
    <ul>
      <li>→ <span>Lorem ipsum dolor sit ameonsec</span></li>
      <li>→ <span>Praesent vestibulum molestie</span></li>
      <li>→ <span>Aenean nonumy hedrerit mauris</span></li>
      <li>→ <span>Phasellus porta. Fusce susci</span></li>
      <li>→ <span>Cum sociis natoque penatibus et</span></li>
      <li>→ <span>Nulla dui. Fusce feugiat masuada</span></li>
      <li>→ <span>Morbi nunc odio gravida aursu</span></li>
      <li>→ <span>Maecenas tristique orci ac sem</span></li>
      <li>→ <span>Duis ultricies pharetra magna</span></li>
      <li>→ <span>Lorem ipsum dolor sit amet, cons</span></li>
      <li>→ <span>Mauris fermentm dictum magna</span></li>
      <li>→ <span>Sed laoreet aliquam leo tellus dol</span></li>
      <li>→ <span>Aenean auctor wisi et urna</span></li>
      <li>→ <span>Aliquam erat volatuis ac turpis</span></li>
    </ul>
    <a class="more orange" style="margin-top:24px"><span class="dot"></span>All Services</a>
    <div class="double-rule" style="margin-top:28px"></div>
  </section>

  <section class="abs contacts">
    <h2 class="heading"><svg width="15" height="12" viewBox="0 0 15 12"><rect x="0.5" y="0.5" width="14" height="11" fill="none" stroke="#333"/><path d="M0.5 0.5l7 6 7-6" fill="none" stroke="#333"/></svg>Contacts</h2>
    <address>4120 Quarry Lane Place,<br>Lithgow, NS 27 Rd 19</address>
    <dl>
      <dt>Freephone:</dt><dd>+1 800 555 0142</dd>
      <dt>Telephone:</dt><dd>+1 800 555 0178</dd>
      <dt>FAX:</dt><dd>+1 800 555 0193</dd>
    </dl>
  </section>
</aside>

<main class="abs col-center">
  <section class="abs" style="left:14px;top:28px;width:390px">
    <h2 class="heading">Welcome</h2>
    <div class="abs thumb" role="img" aria-label="Large mining dump truck" style="left:0;top:40px;width:120px;height:140px"></div>
    <div class="abs" style="left:130px;top:40px;width:262px">
      <a class="text-link">Lorem ipsum dolor sit amet, consesent ves tibulum molestie lacus. Aenean nonummy</a>
      <p class="body-copy" style="margin-top:14px">Lorem ipsum dolor sit amet, consectetuer adipi scing elit. Praesent vestibu luolestie lacuenean nonummy ndrerit maursellus porta. Fusc uscipit varius mi. Cum sociis natoque penatibus et magis dis parturient montes, nascetur ridiculus mus. Nulla dui.</p>
    </div>
    <div class="abs link-row" style="left:0;top:206px"><a class="more"><span class="dot"></span>Read More About Us</a><a class="more"><span class="dot"></span>Company History</a></div>
    <div class="abs divider" style="left:0;top:250px;width:392px"></div>
  </section>

  <section class="abs" style="left:14px;top:307px;width:392px">
    <h2 class="heading">Our Objects</h2>
    <a class="text-link" style="display:block;margin-top:16px">Sed ut perspiciatis unde omnis iste natus error sit voluptatem accusan tium doloremque laudantium, totam rem aperi</a>
    <p class="body-copy">Lorem ipsum dolor sit amet, consectetuer adipi scing elit. Praesent vestibu luolestie lacuenean nonummy ndrerit maursellus porta. Fusc uscipit varius mi. Cum sociis natoque penatibus et mag.</p>
    <a class="more" style="color:var(--link-grey);margin-top:24px"><span class="dot" style="background:#888"></span>Read More</a>
    <div class="divider" style="margin-top:28px"></div>
  </section>

  <section class="abs" style="left:14px;top:520px;width:392px">
    <h2 class="heading">Investors</h2>
    <div style="display:flex;gap:10px;margin-top:18px">
      <div class="investor" role="img" aria-label="Portrait of investor Dale Hurworth in hard hat" style="background:linear-gradient(#b59a6a,#c98a50)"></div>
      <div class="investor" role="img" aria-label="Portrait of investor Neil Brannock" style="background:linear-gradient(#e8eef2,#c8b8a8)"></div>
      <div class="investor" role="img" aria-label="Portrait of investor Ross Kettering in suit" style="background:linear-gradient(#d8d8d8,#7a7a80)"></div>
    </div>
    <div class="link-row" style="margin-top:26px;gap:32px"><a class="more"><span class="dot"></span>Dale Hurworth</a><a class="more"><span class="dot"></span>Neil Brannock</a><a class="more"><span class="dot"></span>Ross Kettering</a></div>
  </section>
  <div class="abs divider" style="left:0;bottom:0;width:434px;height:22px;background:#262626"></div>
</main>

<aside class="abs col-right">
  <section class="abs login">
    <h2 class="heading" style="margin-bottom:10px"><svg width="12" height="14" viewBox="0 0 12 14"><circle cx="6" cy="3.5" r="2.5" fill="none" stroke="#333"/><path d="M2 13V8h8v5" fill="none" stroke="#333"/></svg>Login</h2>
    <div class="field"><span>Username</span><div></div></div>
    <div class="field"><span>Password</span><div></div></div>
    <p style="font-size:11px;margin-top:18px"><a style="color:var(--link-orange);text-decoration:underline">Lost Password?</a> &nbsp;| &nbsp;No account yet? <a style="color:var(--link-orange);text-decoration:underline">Register</a></p>
    <div class="btn-orange" style="margin:20px 0 0 156px;width:60px;height:20px;line-height:20px">Login</div>
    <div class="double-rule" style="margin-top:20px"></div>
  </section>

  <section class="abs jobs">
    <h2 class="heading" style="margin-bottom:8px"><svg width="14" height="14" viewBox="0 0 14 14"><circle cx="6" cy="6" r="4.5" fill="none" stroke="#333" stroke-width="1.5"/><path d="M9 9l4 4" stroke="#333" stroke-width="2"/></svg>Job Application</h2>
    <div class="job"><a>Lorem ipsum dolor sit amet, consec</a><time>Tue Sep 16, 2008</time></div>
    <div class="job"><a>Praesent vestibulum molestie lacus</a><time>Tue Sep 16, 2008</time></div>
    <div class="job"><a>Aenean nonumm hendrerit mauris</a><time>Tue Sep 16, 2008</time></div>
    <div class="job"><a>Vestibulum molestie lacusene</a><time>Tue Sep 16, 2008</time></div>
    <div class="job"><a>Phasellus porta. Fusce suscipit varius</a><time>Tue Sep 16, 2008</time></div>
    <div class="job" style="border:0"><a>Fusce suscipit varius mi. Cum soci</a><time>Tue Sep 16, 2008</time></div>
    <a class="more orange" style="margin-top:16px;font-weight:700;font-size:11px"><span class="dot"></span>ALL JOBS</a>
  </section>
</aside>

<footer class="abs footer">Ironbark Shift Workforce © 2014 .- Privacy Policy</footer>

</body>
</html>
```